Business Card Design - Law Firm

We are a boutique law firm located near the beach in Manly, Australia. We have recently had a new logo designed and are revamping our business cards with the new logo.

We have recently had a business card design done for us but are not entirely happy with it. We are looking for something modern, simplistic but striking. We would like to see multiple designs.

We have attached a word document which includes our new logo and the current business card design which we are looking at moving away from.

We would like the business cards to be double sided. We would like the design to include something which we can print in gloss colour when we send it to the business card printers.

```html
<!DOCTYPE html>
<html lang="en">
<head>
<meta charset="utf-8">
<title>Corran &amp; Associates Lawyers – Business Card</title>
<link href="https://fonts.googleapis.com/css2?family=Arimo:wght@400;700&display=swap" rel="stylesheet">
<style>
  :root {
    --navy: #3a4691;
    --navy-deep: #2e3a85;
    --mauve: #8a8290;
    --gold: #c6ae74;
    --gold-light: #ebe3c8;
    --paper: #fbfaf7;
    --panel-cool: #efeef4;
    --panel-warm: #f3efe3;
    --backdrop: #e6e5e1;
  }
  * { box-sizing: border-box; margin: 0; padding: 0; }
  html, body {
    width: 1200px;
    height: 873px;
    overflow: hidden;
  }
  body {
    background: var(--backdrop);
    font-family: "Arimo", Arial, sans-serif;
    position: relative;
  }
  .card {
    position: absolute;
    top: 158px;
    width: 340px;
    height: 556px;
    background: var(--paper);
    box-shadow: 0 6px 18px rgba(0, 0, 0, 0.18);
  }

  /* ---------- Back: contact details ---------- */
  .card--details { left: 215px; }
  .details__frame {
    position: absolute;
    inset: 8px;
    background:
      linear-gradient(to bottom, rgba(240, 236, 225, 0) 35%, rgba(240, 236, 225, 0.85) 100%),
      linear-gradient(to right, var(--navy) 0%, var(--mauve) 40%, var(--gold) 78%, var(--gold-light) 100%);
  }
  .details__top-bar {
    position: absolute;
    top: 14px;
    left: 14px;
    right: 58px;
    height: 42px;
    background: var(--paper);
  }
  .details__panel {
    position: absolute;
    top: 74px;
    left: 34px;
    right: 10px;
    bottom: 14px;
    background: linear-gradient(to right, var(--panel-cool) 0%, #f7f6f3 65%, var(--panel-warm) 100%);
    color: var(--navy);
    text-align: center;
  }
  .contact { padding-top: 60px; }
  .contact__name {
    font-size: 25px;
    font-weight: 400;
    letter-spacing: 0.5px;
    text-transform: uppercase;
  }
  .contact__role { font-size: 16px; margin-top: 2px; }
  .contact__phone { font-size: 20px; margin-top: 22px; letter-spacing: 0.5px; }
  .contact__line { font-size: 13.5px; margin-top: 6px; }
  .contact__line + .contact__line { margin-top: 4px; }
  .contact__address { font-size: 15.5px; margin-top: 24px; line-height: 1.15; }
  .details__firm {
    position: absolute;
    right: 18px;
    bottom: 40px;
    color: var(--gold);
    font-weight: 700;
    font-size: 18px;
    text-align: center;
    line-height: 1.3;
  }
  .details__firm-sub { display: block; font-size: 12px; letter-spacing: 9px; margin-right: -9px; }

  /* ---------- Front: firm name ---------- */
  .card--brand { left: 645px; }
  .brand__field {
    position: absolute;
    top: 12px;
    left: 12px;
    right: 12px;
    height: 404px;
    background: linear-gradient(to top right, var(--navy-deep) 12%, var(--mauve) 45%, var(--gold) 72%, var(--gold-light) 100%);
  }
  .brand__mark {
    position: absolute;
    top: 52px;
    right: 62px;
    width: 64px;
    height: 64px;
    border-radius: 50%;
    background: var(--navy);
  }
  .brand__name {
    position: absolute;
    top: 96px;
    left: 104px;
    writing-mode: vertical-rl;
    color: var(--paper);
    font-weight: 700;
    font-size: 26px;
    line-height: 1.25;
  }
  .brand__name-sub { font-size: 17px; letter-spacing: 14px; }
  .brand__bar {
    position: absolute;
    left: 12px;
    right: 12px;
    bottom: 12px;
    height: 60px;
    background: linear-gradient(to right, var(--navy) 0%, var(--mauve) 45%, var(--gold) 80%, var(--gold-light) 100%);
  }
</style>
</head>
<body>

  <article class="card card--details" aria-label="Business card, contact side">
    <div class="details__frame">
      <div class="details__top-bar"></div>
      <div class="details__panel">
        <div class="contact">
          <p class="contact__name">Nadia Whitlow</p>
          <p class="contact__role">Practice Manager</p>
          <p class="contact__phone">(02) 9000 4817</p>
          <p class="contact__line">nadia.whitlow@corranlaw.com.au</p>
          <p class="contact__line">www.corranassociates.com.au</p>
          <p class="contact__address">Suite 4, 18 Wharf Row<br>SEAVIEW NSW 2090</p>
        </div>
        <p class="details__firm">Corran &amp; Associates<span class="details__firm-sub">LAWYERS</span></p>
      </div>
    </div>
  </article>

  <article class="card card--brand" aria-label="Business card, brand side">
    <div class="brand__field">
      <span class="brand__mark"></span>
      <p class="brand__name">Corran &amp; Associates<br><span class="brand__name-sub">LAWYERS</span></p>
    </div>
    <div class="brand__bar"></div>
  </article>

</body>
</html>
```